Larkspur Vale Management

I need a professional website. My current website is larkspurvalemanagement.com and I hate it. It was created with some AI tool very quickly because I needed a site up and running with no advanced notice. I’m open to all designs .. I trust you, the professionals will deliver the results I’m anxiously awaiting! :)

```html
<!DOCTYPE html>
<html lang="en">
<head>
<meta charset="utf-8">
<title>Larkspur Vale Management</title>
<link href="https://fonts.googleapis.com/css2?family=Poppins:wght@400;500;600;700&display=swap" rel="stylesheet">
<style>
:root{
  --navy:#233a63;
  --navy-deep:#1b2d4f;
  --footer:#1f2b45;
  --red:#d0272e;
  --ink:#1c1c1c;
  --muted:#555b66;
  --card:#f1f2f4;
  --line:#e3e5e9;
  --white:#ffffff;
  --star:#e0b53a;
}
*{margin:0;padding:0;box-sizing:border-box}
html,body{width:1200px;height:3781px;overflow:hidden}
body{position:relative;font-family:'Poppins',sans-serif;color:var(--ink);background:var(--white)}
.abs{position:absolute}
.btn{position:absolute;background:var(--red);color:var(--white);font-size:11px;font-weight:600;display:flex;align-items:center;justify-content:center;text-transform:uppercase;letter-spacing:.2px;border-radius:2px}

/* header */
.brand{left:161px;top:22px;width:120px;height:80px;display:flex;align-items:center;gap:8px}
.brand-mark{width:14px;height:14px;background:var(--navy);border-radius:50%;flex:none}
.brand-name{font-weight:700;font-size:17px;line-height:1.1;color:var(--navy)}
.contact{display:flex;align-items:center;gap:8px;top:24px}
.contact .ico{width:36px;height:36px;border-radius:50%;background:var(--navy);display:flex;align-items:center;justify-content:center}
.contact small{display:block;font-size:11px;color:var(--muted)}
.contact b{display:block;font-size:15px;font-weight:500;color:var(--ink)}
.nav{top:89px;font-size:13px}
.nav a{position:absolute;white-space:nowrap;color:var(--ink);text-decoration:none}
.nav a.active{color:var(--red)}

/* hero */
.hero{left:0;top:125px;width:1200px;height:667px;background:linear-gradient(100deg,#1d2f4e 0%,#2f4566 45%,#5d6e80 75%,#39404a 100%)}
.hero-title{left:158px;top:278px;font-size:39px;font-weight:600;line-height:48px;color:var(--white);text-transform:uppercase}
.hero-sub{left:161px;top:428px;font-size:13px;color:var(--white)}
.hero-arrow{top:398px;color:var(--white);font-size:28px}

/* section headings */
.heading{position:absolute;left:0;width:1200px;text-align:center}
.heading .ghost{position:absolute;left:0;right:0;font-size:50px;font-weight:600;color:#f0f1f3;text-transform:uppercase;top:-18px}
.heading h2{position:relative;font-size:32px;font-weight:600;text-transform:uppercase;color:var(--ink)}
.heading .bar{width:62px;height:3px;background:var(--navy);margin:10px auto 0}
.heading.dark .ghost{color:rgba(255,255,255,.12)}
.heading.dark h2{color:var(--white)}
.heading.dark .bar{background:var(--red)}

/* about */
.about-img{left:0;top:770px;width:631px;height:526px;background:linear-gradient(120deg,#2a3b45 0%,#4a5a63 40%,#353b44 70%,#e8eaec 100%)}
.about-head{left:681px;top:915px}
.about-head .ghost{position:absolute;left:0;top:-8px;font-size:50px;font-weight:600;color:#f0f1f3;white-space:nowrap}
.about-head h2{position:relative;font-size:32px;font-weight:600;white-space:nowrap}
.about-head .bar{width:62px;height:3px;background:var(--navy);margin-top:6px}
.about-text{left:681px;top:996px;width:365px;font-size:13.5px;line-height:19.5px;color:var(--muted)}

/* steps */
.step{position:absolute;top:1498px;width:277px;height:273px;background:var(--card);border-radius:6px;text-align:center}
.step.featured{background:linear-gradient(#ffffff,#fbe7e8);border:1px solid #e9a9ac}
.step .circle{width:86px;height:86px;border-radius:50%;background:var(--navy);border:4px solid #c9cfdb;margin:31px auto 0;display:flex;align-items:center;justify-content:center}
.step.featured .circle{background:var(--red);border-color:#f2b6b8}
.step h3{font-size:18px;font-weight:500;margin-top:40px}
.step p{font-size:13.5px;line-height:19.5px;color:var(--muted);padding:4px 22px 0}

/* services */
.services-band{left:0;top:1808px;width:1200px;height:833px;background:linear-gradient(180deg,var(--navy) 0%,#2a4068 50%,#263a5d 100%)}
.svc{position:absolute;top:2082px;width:277px;height:325px;background:var(--white);border-radius:3px;overflow:hidden;text-align:center}
.svc .ph{height:179px}
.svc h3{font-size:17px;font-weight:500;line-height:20px;margin-top:10px;padding:0 20px}
.svc p{font-size:11.5px;line-height:14px;color:var(--muted);margin-top:8px;padding:0 34px}
.svc .more{display:block;font-size:11.5px;font-weight:600;color:var(--navy);margin-top:10px}
.svc-arrow{position:absolute;top:2226px;width:38px;height:38px;border-radius:50%;background:var(--white);display:flex;align-items:center;justify-content:center}

/* testimonials */
.quote{position:absolute;top:2788px;width:277px;height:198px;border:1px solid var(--line);border-radius:3px;padding:24px 24px}
.quote b{display:block;font-size:13px;font-weight:500}
.quote .role{font-size:11.5px;margin-top:6px}
.quote .stars{color:var(--star);font-size:14px;letter-spacing:1px;margin-top:5px}
.quote p{font-size:12px;line-height:15px;color:var(--muted);margin-top:14px}
.dots{left:566px;top:3011px;display:flex;gap:9px}
.dots i{width:18px;height:3px;background:var(--navy)}
.dots i.on{background:var(--red)}

/* newsletter */
.news-text{left:270px;top:3164px;width:660px;text-align:center;font-size:11.5px;line-height:15px;color:var(--muted)}
.news-input{left:304px;top:3239px;width:428px;height:36px;background:#ebebeb;border-radius:2px;font-size:12px;color:#444;padding:11px 18px}

/* footer */
.footer{left:0;top:3320px;width:1200px;height:461px;background:var(--footer)}
.foot-brand{left:161px;top:3440px;display:flex;align-items:center;gap:10px}
.foot-brand .brand-mark{width:18px;height:18px;background:var(--white)}
.foot-brand span{font-weight:700;font-size:20px;line-height:1.1;color:var(--white)}
.foot-contact{top:3500px;display:flex;align-items:center;gap:10px;color:var(--white);font-size:12.5px}
.foot-contact .ico{width:27px;height:27px;border-radius:50%;background:var(--white);display:flex;align-items:center;justify-content:center}
.foot-rule{height:1px;background:#3e4a63}
.foot-text{left:161px;top:3592px;width:300px;font-size:12.5px;line-height:18.5px;color:var(--white)}
.foot-link{font-size:12.5px;color:var(--white);white-space:nowrap}
.social{top:3667px;width:15px;height:15px;border:2px solid var(--white);border-radius:50%}
.copyright{left:161px;top:3743px;font-size:11.5px;color:var(--white)}
.foot-img{left:792px;top:3537px;width:408px;height:244px;background:linear-gradient(160deg,#1f2b45 0%,#3e5660 55%,#2a363f 100%);clip-path:polygon(40% 100%,62% 45%,82% 0,100% 22%,100% 100%)}
</style>
</head>
<body>

<!-- header -->
<div class="abs brand"><span class="brand-mark"></span><span class="brand-name">LARKSPUR<br>VALE</span></div>
<div class="abs contact" style="left:591px">
  <span class="ico"><svg width="16" height="16" viewBox="0 0 24 24" fill="#fff"><path d="M6.6 10.8a15 15 0 0 0 6.6 6.6l2.2-2.2a1 1 0 0 1 1-.25 11.4 11.4 0 0 0 3.6.57 1 1 0 0 1 1 1V20a1 1 0 0 1-1 1A17 17 0 0 1 3 4a1 1 0 0 1 1-1h3.5a1 1 0 0 1 1 1c0 1.25.2 2.45.57 3.57a1 1 0 0 1-.25 1z"/></svg></span>
  <span><small>Call Us</small><b>555-014-2290</b></span>
</div>
<div class="abs contact" style="left:772px">
  <span class="ico"><svg width="16" height="12" viewBox="0 0 16 12" fill="none" stroke="#fff" stroke-width="1.6"><rect x="1" y="1" width="14" height="10" rx="1"/><path d="M1 1l7 6 7-6"/></svg></span>
  <span><small>E-Mail</small><b>info@larkspurvalemgmt.com</b></span>
</div>
<nav class="abs nav" style="left:0;width:1200px">
  <a class="active" style="left:380px">Home</a>
  <a style="left:481px">About Us</a>
  <a style="left:606px">Services</a>
  <a style="left:726px">Testimonial</a>
  <a style="left:863px">News</a>
  <a style="left:963px">Contact Us</a>
</nav>

<!-- hero -->
<div class="abs hero" role="img" aria-label="Modern multi-storey apartment building at dusk with lit windows and trees"></div>
<svg class="abs" style="left:0;top:125px" width="1200" height="667" viewBox="0 0 1200 667">
  <polygon points="0,545 1200,575 1200,667 0,667" fill="#fff"/>
  <polygon points="0,550 176,582 0,642" fill="var(--navy)"/>
  <polygon points="858,667 1200,548 1200,667" fill="var(--navy)"/>
</svg>
<div class="abs hero-arrow" style="left:28px">&#8249;</div>
<div class="abs hero-arrow" style="left:1156px">&#8250;</div>
<h1 class="abs hero-title">Professional Property<br>Management You<br>Can Trust</h1>
<p class="abs hero-sub">A true partner, not just a vendor.</p>
<a class="btn" style="left:161px;top:470px;width:197px;height:36px">Get a Free Consultation</a>

<!-- about -->
<div class="abs about-img" role="img" aria-label="Two smiling business professionals with arms crossed in front of a glass tower"></div>
<div class="abs about-head"><span class="ghost">ABOUT US</span><h2>ABOUT US</h2><div class="bar"></div></div>
<p class="abs about-text">Lorem Ipsum is simply dummy text of the printing and typesetting industry. Lorem Ipsum has been the industry's standard dummy text ever since the 1500s, when an unknown printer took a galley of type and scrambled it to make a type specimen book. It has survived not only five centuries, but also the leap into electronic typesetting, remaining essentially unchanged. It was popularised in the 1960s with the release of Quillmark sheets containing Lorem Ipsum passages, and more recently with desktop publishing software like Folio Press including versions of Lorem Ipsum.</p>
<a class="btn" style="left:681px;top:1259px;width:137px;height:37px">Learn More</a>

<!-- how it works -->
<div class="heading" style="top:1392px"><span class="ghost">How It Works</span><h2>How It Works</h2><div class="bar"></div></div>
<div class="step" style="left:161px">
  <div class="circle"><svg width="30" height="30" viewBox="0 0 24 24" fill="#fff"><path d="M6.6 10.8a15 15 0 0 0 6.6 6.6l2.2-2.2a1 1 0 0 1 1-.25 11.4 11.4 0 0 0 3.6.57 1 1 0 0 1 1 1V20a1 1 0 0 1-1 1A17 17 0 0 1 3 4a1 1 0 0 1 1-1h3.5a1 1 0 0 1 1 1c0 1.25.2 2.45.57 3.57a1 1 0 0 1-.25 1z"/></svg></div>
  <h3>Schedule a Consultation</h3>
  <p>Lorem Ipsum is simply dummy text of the printing and typesetting industry.</p>
</div>
<div class="step featured" style="left:461px">
  <div class="circle"><svg width="28" height="30" viewBox="0 0 28 30" fill="none" stroke="#fff" stroke-width="2"><rect x="6" y="2" width="16" height="22" rx="1"/><path d="M10 8h8M10 13h8M10 18h8M2 28h24"/></svg></div>
  <h3>Property Assessment</h3>
  <p>Lorem Ipsum is simply dummy text of the printing and typesetting industry.</p>
</div>
<div class="step" style="left:762px">
  <div class="circle"><svg width="30" height="30" viewBox="0 0 30 30" fill="#fff"><circle cx="15" cy="11" r="6"/><path d="M4 28c0-6 5-9 11-9s11 3 11 9z"/><path d="M7 12a8 8 0 0 1 16 0" fill="none" stroke="#fff" stroke-width="2"/></svg></div>
  <h3>Reports &amp; Support</h3>
  <p>Lorem Ipsum is simply dummy text of the printing and typesetting industry.</p>
</div>

<!-- services -->
<div class="abs services-band" role="img" aria-label="Blue-tinted city skyline behind the services section"></div>
<svg class="abs" style="left:0;top:1808px" width="1200" height="833" viewBox="0 0 1200 833">
  <polygon points="0,0 1200,0 1200,8 968,112 170,18 0,22" fill="#fff"/>
  <polygon points="170,18 968,104 1165,12 975,124 170,26" fill="var(--red)"/>
  <polygon points="0,833 0,825 285,740 1080,810 1200,833" fill="#fff"/>
  <polygon points="40,830 285,735 1080,805 285,752" fill="var(--red)"/>
</svg>
<div class="heading dark" style="top:1986px"><span class="ghost">Our Services</span><h2>Our Services</h2></div>
<div class="svc" style="left:161px">
  <div class="ph" role="img" aria-label="White two-storey family home with a dark roof" style="background:linear-gradient(#9fb2c7,#d9dde2 60%,#6f7b6b)"></div>
  <h3>Residential Property<br>Management</h3>
  <p>It is a long established fact that a looking at its layout.</p>
  <span class="more">SEE MORE</span>
</div>
<div class="svc" style="left:461px">
  <div class="ph" role="img" aria-label="Modern commercial apartment block with brick and glass facade" style="background:linear-gradient(90deg,#2e4664,#4d6f8a 45%,#b58a6e 75%,#7a8ea3)"></div>
  <h3>Commercial Property<br>Management</h3>
  <p>It is a long established fact that a looking at its layout.</p>
  <span class="more">SEE MORE</span>
</div>
<div class="svc" style="left:762px">
  <div class="ph" role="img" aria-label="Agent reviewing documents with a couple at a table" style="background:linear-gradient(90deg,#c9b79f,#e6dccd 50%,#d7cfc4)"></div>
  <h3>Tenant<br>Placement</h3>
  <p>It is a long established fact that a looking at its layout.</p>
  <span class="more">SEE MORE</span>
</div>
<div class="svc-arrow" style="left:98px"><svg width="10" height="14" viewBox="0 0 10 14" fill="none" stroke="#333" stroke-width="1.5"><path d="M8 1L2 7l6 6"/></svg></div>
<div class="svc-arrow" style="left:1061px"><svg width="10" height="14" viewBox="0 0 10 14" fill="none" stroke="#333" stroke-width="1.5"><path d="M2 1l6 6-6 6"/></svg></div>
<a class="btn" style="left:524px;top:2446px;width:153px;height:34px">View All Services</a>

<!-- testimonials -->
<div class="heading" style="top:2690px"><span class="ghost">What Our Clients Say</span><h2>What Our Clients Say</h2></div>
<div class="quote" style="left:161px"><b>Jordan P</b><div class="role">VP of Sales at a Mid-Sized B2B Firm</div><div class="stars">★★★★★</div><p>Completely transformed our lead generation efforts. We've seen a 35% increase in high-quality leads in just three months.</p></div>
<div class="quote" style="left:461px"><b>Jordan P</b><div class="role">VP of Sales at a Mid-Sized B2B Firm</div><div class="stars">★★★★★</div><p>Completely transformed our lead generation efforts. We've seen a 35% increase in high-quality leads in just three months.</p></div>
<div class="quote" style="left:762px"><b>Jordan P</b><div class="role">VP of Sales at a Mid-Sized B2B Firm</div><div class="stars">★★★★★</div><p>Completely transformed our lead generation efforts. We've seen a 35% increase in high-quality leads in just three months.</p></div>
<div class="abs dots"><i></i><i class="on"></i><i></i></div>

<!-- newsletter -->
<div class="heading" style="top:3082px"><span class="ghost">Newsletter Sign Up</span><h2>Newsletter Sign Up</h2><div class="bar" style="background:var(--red)"></div></div>
<p class="abs news-text">It is a long established fact that a reader will be distracted by the readable content of a page when looking at its layout. The point of using Lorem Ipsum is that it has a more-or-less normal distribution of letters, as opposed to using 'Content here, content here', making it look like readable English.</p>
<div class="abs news-input">Email Address</div>
<a class="btn" style="left:744px;top:3239px;width:151px;height:36px">Subscribe Now</a>

<!-- footer -->
<div class="abs footer"></div>
<svg class="abs" style="left:0;top:3320px" width="1200" height="120" viewBox="0 0 1200 120">
  <polygon points="0,0 1200,0 1200,0 868,112 160,22 0,14" fill="#fff"/>
  <polygon points="160,20 868,104 1165,6 880,120 160,28" fill="var(--red)"/>
</svg>
<div class="abs foot-img" role="img" aria-label="Glass skyscraper rising into the corner"></div>
<div class="abs foot-brand"><span class="brand-mark"></span><span>LARKSPUR<br>VALE</span></div>
<div class="abs foot-contact" style="left:609px">
  <span class="ico"><svg width="13" height="13" viewBox="0 0 24 24" fill="var(--footer)"><path d="M6.6 10.8a15 15 0 0 0 6.6 6.6l2.2-2.2a1 1 0 0 1 1-.25 11.4 11.4 0 0 0 3.6.57 1 1 0 0 1 1 1V20a1 1 0 0 1-1 1A17 17 0 0 1 3 4a1 1 0 0 1 1-1h3.5a1 1 0 0 1 1 1c0 1.25.2 2.45.57 3.57a1 1 0 0 1-.25 1z"/></svg></span>+1 555 013 7720
</div>
<div class="abs foot-contact" style="left:773px">
  <span class="ico"><svg width="13" height="10" viewBox="0 0 16 12" fill="none" stroke="var(--footer)" stroke-width="1.8"><rect x="1" y="1" width="14" height="10" rx="1"/><path d="M1 1l7 6 7-6"/></svg></span>info@larkspurvalemanagement.com
</div>
<div class="abs foot-rule" style="left:161px;top:3559px;width:876px"></div>
<p class="abs foot-text">It is a long established fact that a reader will be distracted by the readable content of a page when looking at its layout.</p>
<span class="abs foot-link" style="left:591px;top:3590px">Home</span>
<span class="abs foot-link" style="left:690px;top:3590px">How It Work</span>
<span class="abs foot-link" style="left:591px;top:3628px">About Us</span>
<span class="abs foot-link" style="left:690px;top:3628px">Contact Us</span>
<span class="abs foot-link" style="left:591px;top:3665px">Services</span>
<span class="abs social" style="left:161px"></span>
<span class="abs social" style="left:203px"></span>
<span class="abs social" style="left:244px"></span>
<div class="abs foot-rule" style="left:161px;top:3725px;width:583px"></div>
<p class="abs copyright">Copyright © 2026 Larkspur Vale Management LLC. All rights reserved.</p>

</body>
</html>
```